WALKING FOOD TOURISM BUSINESS. REQUEST FOR DIGITAL BROCHURE

Our business is a walking food tourism business in and around Melbourne's central city. We are needing a e-digital brochure - to be solely used as email' marketing content, not print. Therefore PDF size needs to be appropriate/suitable. Please see attached written content required for the brochure - together with our logo. For images, I am happy for designer to use our website content (www.wanderplatekitchen.com). OR any other appropriate and creative 'foodie' or Melbourne image suitable. Many thanks:)

Target Market(s)

Premium brand travellers or local adventurous Australians.

Requirements
Must have
• Quality font and images
Nice to have
• Quality Melbourne and food images. See website - wanderplatekitchen.com
Should not have
• Too much colour. Brand is black and white, sophisticated, premium product.

```html
<!DOCTYPE html>
<html lang="en">
<head>
<meta charset="utf-8">
<title>Wanderplate Kitchen – Walking Food Tours Brochure</title>
<link href="https://fonts.googleapis.com/css2?family=Lexend:wght@300;400;500;600&display=swap" rel="stylesheet">
<style>
  :root {
    --ink: #0b0b0b;
    --paper: #ffffff;
    --backdrop: #f2f2f2;
    --band: #f1f1f3;
    --muted: #8a8a8a;
    --headline-light: #7a7a7a;
    --photo-sky: #b9c8e4;
    --photo-stone: #9a9588;
    --photo-tree: #4a3a2a;
    --photo-lawn: #5f8a2e;
  }
  * { box-sizing: border-box; margin: 0; padding: 0; }
  html, body {
    width: 1200px; height: 840px; overflow: hidden;
    background: var(--backdrop);
    font-family: "Lexend", "Helvetica Neue", Arial, sans-serif;
    color: var(--ink);
  }
  .brochure {
    position: absolute; left: 317px; top: 20px;
    width: 566px; height: 800px;
    background: var(--paper);
    box-shadow: 0 6px 24px rgba(0,0,0,.12);
    overflow: hidden;
  }
  .hero-photo {
    position: absolute; left: 0; top: 0; width: 566px; height: 372px;
    background:
      linear-gradient(to bottom, transparent 78%, var(--photo-lawn) 100%),
      radial-gradient(ellipse at 50% 62%, var(--photo-stone) 0 22%, transparent 45%),
      linear-gradient(90deg, var(--photo-tree) 0%, var(--photo-sky) 30%, var(--photo-sky) 70%, var(--photo-tree) 100%);
  }
  .brand-mark {
    position: absolute; left: 35px; top: 8px; width: 150px; height: 63px;
    background: var(--ink); color: var(--paper);
    display: flex; align-items: center; justify-content: center;
    font-size: 14px; font-weight: 500; letter-spacing: .3px; text-align: center; line-height: 1.2;
  }
  .features { position: absolute; top: 304px; left: 36px; display: flex; gap: 14px; }
  .feature {
    width: 156px; height: 121px; background: var(--paper);
    border-bottom: 4px solid var(--ink);
    display: flex; flex-direction: column; align-items: center; padding-top: 18px;
  }
  .feature svg { width: 34px; height: 34px; }
  .feature-label { margin-top: 14px; font-size: 12.5px; font-weight: 500; }
  .about { position: absolute; left: 41px; top: 483px; width: 260px; }
  .about h2 { font-size: 17px; font-weight: 400; margin-bottom: 6px; }
  .about p { font-size: 10.4px; font-weight: 300; line-height: 15.8px; color: var(--muted); text-align: justify; }
  .divider { position: absolute; left: 316px; top: 488px; width: 1px; height: 129px; background: var(--ink); }
  .headline { position: absolute; left: 326px; top: 480px; line-height: 46px; }
  .headline span { display: block; }
  .headline .light { font-size: 32px; font-weight: 300; color: var(--headline-light); }
  .headline .bold { font-size: 33px; font-weight: 600; color: var(--ink); }
  .experiences { position: absolute; left: 0; top: 654px; width: 566px; height: 89px; background: var(--band); }
  .experiences h3 { position: absolute; left: 37px; top: 29px; font-size: 16px; font-weight: 500; }
  .experiences h3::after { content: ""; display: block; width: 26px; height: 3px; background: var(--ink); margin-top: 5px; }
  .tour { position: absolute; display: flex; align-items: center; gap: 6px; font-size: 12.5px; font-style: italic; font-weight: 300; }
  .tour-num {
    width: 24px; height: 24px; border: 2px solid var(--ink); border-radius: 50%;
    font-size: 7.5px; font-style: normal; font-weight: 600;
    display: flex; align-items: center; justify-content: center; position: relative;
  }
  .tour-num::after { content: ""; position: absolute; right: -4px; top: 7px; width: 7px; height: 7px; border-radius: 50%; background: var(--ink); }
  .footer { position: absolute; left: 0; top: 743px; width: 566px; height: 57px; background: var(--ink); color: var(--paper); }
  .footer-cta { position: absolute; left: 37px; top: 10px; font-size: 12px; font-weight: 500; line-height: 18px; }
  .contact { position: absolute; top: 18px; font-size: 9.5px; font-weight: 300; line-height: 13px; }
  .contact strong { display: block; font-weight: 400; }
  .social { position: absolute; left: 393px; top: 8px; font-size: 9.5px; font-weight: 300; }
  .social-row { display: flex; align-items: center; gap: 9px; height: 20px; }
  .social-dot { width: 13px; height: 13px; border: 1px solid var(--paper); border-radius: 50%; }
</style>
</head>
<body>
  <main class="brochure">
    <div class="hero-photo" role="img" aria-label="Photograph of a domed exhibition building behind autumn trees, lawn and fountain"></div>
    <div class="brand-mark">Wanderplate<br>Kitchen</div>

    <section class="features">
      <div class="feature">
        <svg viewBox="0 0 34 34" fill="none" stroke="#0b0b0b" stroke-width="1.8">
          <rect x="3" y="6" width="28" height="25" rx="4"/>
          <line x1="3" y1="13" x2="31" y2="13"/>
          <line x1="10" y1="3" x2="10" y2="9"/><line x1="24" y1="3" x2="24" y2="9"/>
          <g fill="#0b0b0b" stroke="none"><circle cx="11" cy="19" r="1"/><circle cx="17" cy="19" r="1"/><circle cx="23" cy="19" r="1"/><circle cx="11" cy="25" r="1"/><circle cx="17" cy="25" r="1"/><circle cx="23" cy="25" r="1"/></g>
        </svg>
        <span class="feature-label">Always avaliable</span>
      </div>
      <div class="feature">
        <svg viewBox="0 0 34 34" fill="none" stroke="#0b0b0b" stroke-width="1.8">
          <path d="M4 25 A13 13 0 0 1 30 25 Z"/>
          <line x1="2" y1="29" x2="32" y2="29"/>
          <line x1="17" y1="9" x2="17" y2="12"/>
        </svg>
        <span class="feature-label">Wide offer</span>
      </div>
      <div class="feature">
        <svg viewBox="0 0 34 34" fill="none" stroke="#0b0b0b" stroke-width="1.8">
          <circle cx="17" cy="12" r="9"/>
          <path d="M11 19 V32 L17 27 L23 32 V19"/>
        </svg>
        <span class="feature-label">Proffesional service</span>
      </div>
    </section>

    <section class="about">
      <h2>About Us</h2>
      <p>We provide experiential adventure for visitors and locals alike - all through the ‘lens’ of exceptional food. Our tour experiences capture the essence of Melbourne, its people and diverse history - stopping to sip, savour and delight in Melbourne’s foodie hot spots &amp; indulging in their signature tastes.</p>
    </section>
    <div class="divider"></div>
    <h1 class="headline">
      <span class="light">Wanderplate</span>
      <span class="bold">Kitchen</span>
      <span class="light">Experiences!</span>
    </h1>

    <section class="experiences">
      <h3>Our Experiences</h3>
      <div class="tour" style="left:179px;top:13px"><span class="tour-num">01</span>Foodies Bucket List Tour</div>
      <div class="tour" style="left:179px;top:54px"><span class="tour-num">02</span>Street Eats Tour</div>
      <div class="tour" style="left:362px;top:13px"><span class="tour-num">03</span>The Story of Melbourne</div>
      <div class="tour" style="left:360px;top:54px"><span class="tour-num">04</span>Evening Palate &amp; Pairing</div>
    </section>

    <footer class="footer">
      <div class="footer-cta">For Booking<br>Schedule &amp; Enquiry!</div>
      <div class="contact" style="left:174px"><strong>Phone number</strong>+61 400 318 274</div>
      <div class="contact" style="left:258px"><strong>Email</strong>info@wanderplatekitchen.com</div>
      <div class="social">
        <div class="social-row"><span class="social-dot"></span>Wanderplate.Kitchen</div>
        <div class="social-row"><span class="social-dot"></span>wanderplate.kitchen</div>
      </div>
    </footer>
  </main>
</body>
</html>
```